A r&b and house DJ needs a new Graphically pleasing and trendy website for fans and potential client

Want a new design for a dj website. This website wont be updated often so needs to look very graphically pleasing and just be a point of call where fans and potential clients can come and see information about the dj etc.

Needs to have short bio , social network links, and a enquiry button.

You can use some stock images for the moment as some professional images are going to be taken.

Others DJ websites:

https://www.djvornley.com/
http://www.pelkansoutar.com/
http://vomaro.com/
http://uletto.com/
http://www.dorianwelkby.co.uk/gb/home
http://www.fumbrelquix.com/
http://plinvaro.nl/

LOGO LINK IS HERE

https://www.filecrate-example.com/s/kq7wz2m9tnh4xa1/DJ_Vellum_logo.eps?dl=0

Target Market(s)

Fans and also prospective clients ( Nightclubs, Record Labels)

Industry/Entity Type

House

Font styles to use
Sans Serif

Requirements
Must have
• Small Bio, Social Network Links, Enquiry Button.
Nice to have
• Social network links

```html
<!DOCTYPE html>
<html lang="en">
<head>
<meta charset="utf-8">
<title>Velvet Groove DJ</title>
<link href="https://fonts.googleapis.com/css2?family=Raleway:wght@300;400;500;600;700&display=swap" rel="stylesheet">
<style>
:root{
  --ink:#222;
  --white:#fff;
  --dark:#2b2b2b;
  --bar:rgba(40,40,45,.78);
  --panel:rgba(20,18,30,.72);
  --cyan:#3bb9e0;
  --rose:#d0104c;
  --light:#f2f2f2;
  --fb:#1877c9;--tw:#1da1e2;--gp:#e2472f;--sc:#f7781e;
}
*{margin:0;padding:0;box-sizing:border-box}
html,body{width:960px;height:1200px;overflow:hidden}
body{font-family:'Raleway',sans-serif;color:var(--ink);position:relative;background:var(--white)}
.hero{position:absolute;left:0;top:0;width:960px;height:640px;
  background:radial-gradient(ellipse at 30% 30%,#d9b08c 0%,transparent 45%),radial-gradient(ellipse at 75% 35%,#c9434f 0%,transparent 40%),linear-gradient(160deg,#3b2f6e 0%,#6a4f7a 40%,#2c2a55 70%,#1b1d3a 100%)}
.topbar{position:absolute;left:0;top:0;width:960px;height:60px;background:var(--bar)}
.brand{position:absolute;left:48px;top:12px;width:110px;color:var(--white);font-weight:700;font-size:17px;line-height:20px}
.nav{position:absolute;left:180px;top:18px;display:flex;gap:37px;list-style:none}
.nav a{color:var(--white);text-decoration:none;font-weight:700;font-size:20px}
.nav .current{border-bottom:3px solid var(--cyan);padding-bottom:1px}
.social{position:absolute;display:flex;gap:11px;list-style:none}
.social li{width:28px;height:28px;color:var(--white);font-size:6px;font-weight:600;display:flex;align-items:center;justify-content:center;text-align:center;line-height:7px}
.social.top{left:759px;top:16px}
.social.foot{left:600px;top:1130px}
.social.foot li{width:27px;height:27px}
.fb{background:var(--fb)}.tw{background:var(--tw)}.gp{background:var(--gp)}.sc{background:var(--sc)}
.pitch{position:absolute;left:198px;top:352px;width:416px;height:181px;background:var(--panel)}
.note{position:absolute;left:148px;top:375px;width:60px;height:78px;background:var(--white);border-radius:6px;display:flex;align-items:center;justify-content:center}
.pitch h1{position:absolute;left:24px;top:13px;width:390px;font-weight:400;font-size:25px;line-height:31px;color:var(--white)}
.enquiry{position:absolute;left:25px;top:121px;width:242px;height:44px;background:var(--cyan);color:var(--white);font-weight:700;font-size:20px;display:flex;align-items:center;justify-content:center;text-decoration:none}
.player{position:absolute;display:flex;justify-content:space-around;align-items:center;background:#111}
.player.hero-player{left:473px;top:539px;width:141px;height:29px}
.player.foot-player{left:760px;top:1128px;width:143px;height:30px;background:#262626}
.about{position:absolute;left:0;top:640px;width:960px;height:237px;background:var(--light)}
.about .photo{position:absolute;left:98px;top:40px;width:249px;height:166px;background:linear-gradient(135deg,#1c2c5a,#4a3a7a 45%,#8a6a6a 70%,#1a1a2a)}
.about h2{position:absolute;left:385px;top:44px;font-weight:400;font-size:20px;color:var(--rose)}
.about p{position:absolute;left:385px;top:76px;width:510px;font-size:10.4px;line-height:20px}
.more{position:absolute;left:386px;top:166px;width:72px;height:20px;background:var(--rose);color:var(--white);font-size:10.5px;display:flex;align-items:center;justify-content:center;text-decoration:none}
.videos h2{position:absolute;left:0;top:897px;width:960px;text-align:center;font-weight:400;font-size:20px;color:var(--rose)}
.clip{position:absolute;top:943px;width:155px;height:104px;display:flex;align-items:center;justify-content:center}
.c1{left:47px;background:linear-gradient(135deg,#2b2f6a,#8a2a6a,#1a1a3a)}
.c2{left:230px;background:linear-gradient(135deg,#8a4a10,#d07020,#2a1a1a)}
.c3{left:406px;background:linear-gradient(135deg,#1a2a7a,#3a8a5a,#2a1a4a)}
.c4{left:578px;background:linear-gradient(135deg,#6a1a1a,#c04a2a,#2a1a3a)}
.c5{left:755px;background:linear-gradient(135deg,#0a2a6a,#2a5ac0,#0a1a3a)}
.play{width:24px;height:24px;background:rgba(0,0,0,.55);border:1.5px solid var(--white);border-radius:50%;display:flex;align-items:center;justify-content:center;padding-left:2px}
footer{position:absolute;left:0;top:1092px;width:960px;height:108px;background:var(--dark);color:var(--white)}
.foot-brand{position:absolute;left:60px;top:1108px;width:110px;color:var(--white);font-weight:700;font-size:16px;line-height:19px}
.links{position:absolute;top:1105px;list-style:none;font-size:11px;line-height:16.7px;color:var(--white)}
.links.a{left:181px}.links.b{left:261px}
.follow{position:absolute;left:531px;top:1137px;font-size:11px;color:var(--white)}
.copy{position:absolute;left:62px;top:1182px;font-size:9px;color:#bbb}
</style>
</head>
<body>
<div class="hero" role="img" aria-label="Crowd dancing at a club party in front of a DJ at his turntables"></div>
<header class="topbar"></header>
<div class="brand">Velvet Groove<br>DJ</div>
<ul class="nav">
  <li><a class="current" href="#">MUSIC</a></li>
  <li><a href="#">GIGS</a></li>
  <li><a href="#">VIDEOS</a></li>
  <li><a href="#">ABOUT</a></li>
</ul>
<ul class="social top">
  <li class="fb">Friend loop</li><li class="tw">Chirp line</li><li class="gp">Circle plus</li><li class="sc">Wave cast</li>
</ul>

<section class="pitch">
  <h1>Lorem Ipsum is simply dummy text of the printing and typesetting industry</h1>
  <a class="enquiry" href="#">SEND ENQUIRY NOW</a>
</section>
<div class="note">
  <svg width="30" height="46" viewBox="0 0 30 46"><ellipse cx="10" cy="37" rx="9" ry="7" fill="#111"/><rect x="16" y="2" width="3.5" height="36" fill="#111"/><path d="M19 2 C22 10 30 12 27 22 C26 14 22 12 19 12Z" fill="#111"/></svg>
</div>
<div class="player hero-player">
  <svg width="8" height="8" viewBox="0 0 8 8"><rect width="1.5" height="8" fill="#666"/><path d="M8 0V8L2 4Z" fill="#666"/></svg>
  <svg width="8" height="9" viewBox="0 0 8 9"><path d="M0 0V9L8 4.5Z" fill="#fff"/></svg>
  <svg width="8" height="8" viewBox="0 0 8 8"><path d="M0 0V8L6 4Z" fill="#666"/><rect x="6.5" width="1.5" height="8" fill="#666"/></svg>
  <svg width="9" height="7" viewBox="0 0 9 7"><rect width="9" height="1.4" fill="#fff"/><rect y="2.8" width="9" height="1.4" fill="#fff"/><rect y="5.6" width="9" height="1.4" fill="#fff"/></svg>
</div>

<section class="about">
  <div class="photo" role="img" aria-label="DJ mixing at the decks while a crowd parties behind him"></div>
  <h2>About Velvet Groove DJ</h2>
  <p>Lorem Ipsum is simply dummy text of the printing and typesetting industry. Lorem Ipsum has been the industry's standard dummy text ever since the 1500s, when an unknown printer took a galley of type and scrambled it to make a type specimen book. It has survived not only five centuries, but also the leap into electronic typesetting, remaining essentially unchanged.</p>
  <a class="more" href="#">Read More</a>
</section>

<section class="videos">
  <h2>Our Videos</h2>
  <div class="clip c1" role="img" aria-label="Band performing on a stage under coloured lights"><span class="play"><svg width="8" height="9" viewBox="0 0 8 9"><path d="M0 0V9L8 4.5Z" fill="#fff"/></svg></span></div>
  <div class="clip c2" role="img" aria-label="Guitarist singing under warm stage lights"><span class="play"><svg width="8" height="9" viewBox="0 0 8 9"><path d="M0 0V9L8 4.5Z" fill="#fff"/></svg></span></div>
  <div class="clip c3" role="img" aria-label="Drummer and guitarist on a green lit stage"><span class="play"><svg width="8" height="9" viewBox="0 0 8 9"><path d="M0 0V9L8 4.5Z" fill="#fff"/></svg></span></div>
  <div class="clip c4" role="img" aria-label="Band playing live under red stage lights"><span class="play"><svg width="8" height="9" viewBox="0 0 8 9"><path d="M0 0V9L8 4.5Z" fill="#fff"/></svg></span></div>
  <div class="clip c5" role="img" aria-label="Musicians on a blue lit concert stage"><span class="play"><svg width="8" height="9" viewBox="0 0 8 9"><path d="M0 0V9L8 4.5Z" fill="#fff"/></svg></span></div>
</section>

<footer></footer>
<div class="foot-brand">Velvet Groove<br>DJ</div>
<ul class="links a"><li>Music</li><li>Gigs</li><li>Videos</li><li>About</li></ul>
<ul class="links b"><li>Contact</li><li>Legal</li><li>News</li><li>Releases</li></ul>
<span class="follow">Folow Us</span>
<ul class="social foot">
  <li class="fb">Friend loop</li><li class="tw">Chirp line</li><li class="gp">Circle plus</li><li class="sc">Wave cast</li>
</ul>
<div class="player foot-player">
  <svg width="8" height="8" viewBox="0 0 8 8"><rect width="1.5" height="8" fill="#777"/><path d="M8 0V8L2 4Z" fill="#777"/></svg>
  <svg width="8" height="9" viewBox="0 0 8 9"><path d="M0 0V9L8 4.5Z" fill="#fff"/></svg>
  <svg width="8" height="8" viewBox="0 0 8 8"><path d="M0 0V8L6 4Z" fill="#777"/><rect x="6.5" width="1.5" height="8" fill="#777"/></svg>
  <svg width="9" height="7" viewBox="0 0 9 7"><rect width="9" height="1.4" fill="#fff"/><rect y="2.8" width="9" height="1.4" fill="#fff"/><rect y="5.6" width="9" height="1.4" fill="#fff"/></svg>
</div>
<span class="copy">Copyright © 2015 SpinWeb</span>
</body>
</html>
```